Daxholm APP redesign and color change

I am looking for a new design for my app. Please see the attached current design.

Currently, I have a functioning app but the colors and design are awful!
The logo is great but the rest of the app needs a refresh.
(Logo hi res not yet available but will upload soon.)
New colors or anything that is cutting edge.

Basically: It is a secure social media app within a school system where the teachers, students and parents can text, exchange photos, plan curriculum, etc.

I NEED ONLY landing page with a new look!
Looking for one distinct design for the landing page with new look.
The developer will apply this one design towards the rest of the pages/app screens.

Because part of the social media I need the feel and look of what is now the trend. Something that will attract and keep the client(s) interested. I am really leaving all the creative work to the designer and open to any suggestions.
Updates

Target Market(s)

Schools, community, teachers, students, colleges, sport teams

Industry/Entity Type

Non Profit

Font styles to use
Serif
Sans Serif

Colors

Designer to choose colors to be used in the design.

Requirements
Must have
• Sharp, trendy, millennial feel
Nice to have
• Up to designer
Should not have
• Up to designer

```html
<!DOCTYPE html>
<html lang="en">
<head>
<meta charset="utf-8">
<title>Daxholm – Sign in</title>
<link href="https://fonts.googleapis.com/css2?family=Lato:wght@400;700&family=Roboto:wght@400&display=swap" rel="stylesheet">
<style>
  :root {
    --meadow-light: #c9d96a;
    --meadow-mid: #7f9a2c;
    --meadow-deep: #3f5a12;
    --sky-glow: #eef0c8;
    --band-top: #34470a;
    --band-bottom: #4a6a08;
    --card-bg: rgba(244, 244, 236, 0.86);
    --label-gold: #b5790a;
    --button-gold: #b87a00;
    --ink: #2a2a2a;
    --line: #555555;
    --white: #ffffff;
  }
  * { box-sizing: border-box; margin: 0; padding: 0; }
  html, body { width: 741px; height: 1200px; overflow: hidden; }
  body { font-family: "Lato", sans-serif; background: var(--band-bottom); }

  .screen { position: relative; width: 741px; height: 1200px; overflow: hidden; }

  .hero-photo {
    position: absolute; left: 0; top: 0; width: 741px; height: 1023px;
    background:
      radial-gradient(ellipse 60% 18% at 55% 2%, var(--sky-glow) 0%, rgba(238,240,200,0) 100%),
      linear-gradient(180deg, #5e7a22 0%, #4a6a1a 22%, #8fae3a 40%, var(--meadow-light) 62%, var(--meadow-mid) 85%, #6d8a24 100%);
  }

  .footer-band {
    position: absolute; left: 0; top: 1023px; width: 741px; height: 177px;
    background: linear-gradient(180deg, var(--band-top) 0%, var(--band-bottom) 100%);
  }

  .brand-name {
    position: absolute; left: 0; width: 741px; top: 538px;
    text-align: center; color: var(--white);
    font-family: "Lato", sans-serif; font-weight: 400;
    font-size: 34px; letter-spacing: 16px; padding-left: 16px;
  }

  .login-card {
    position: absolute; left: 93px; top: 653px; width: 555px; height: 317px;
    background: var(--card-bg);
  }
  .field { position: absolute; left: 61px; width: 433px; }
  .field-label {
    font-size: 16px; letter-spacing: 1.6px; color: var(--label-gold);
    font-weight: 400; text-transform: uppercase;
  }
  .field-user { top: 62px; }
  .field-value {
    margin-top: 14px; font-family: "Roboto", sans-serif;
    font-size: 23px; color: var(--ink); padding-bottom: 20px;
    border-bottom: 1.5px solid var(--line);
  }
  .field-pass { top: 203px; }
  .password-dots { margin-top: 24px; }

  .submit-button {
    position: absolute; left: 93px; top: 970px; width: 555px; height: 106px;
    background: var(--button-gold); color: var(--white);
    display: flex; align-items: center; justify-content: space-between;
    padding: 0 60px 0 61px; font-size: 23px;
  }

  .signup-link {
    position: absolute; left: 0; width: 741px; top: 1119px;
    text-align: center; color: var(--white); font-size: 18px;
  }
</style>
</head>
<body>
<main class="screen">
  <div class="hero-photo" role="img" aria-label="Photo of a child reading a book while sitting in a sunlit grassy meadow"></div>
  <div class="footer-band"></div>

  <div class="brand-name">DAXHOLM</div>

  <section class="login-card">
    <div class="field field-user">
      <div class="field-label">Username</div>
      <div class="field-value">nora@daxholm.app</div>
    </div>
    <div class="field field-pass">
      <div class="field-label">Password</div>
      <svg class="password-dots" width="140" height="10" viewBox="0 0 140 10" aria-label="Hidden password">
        <g fill="#2a2a2a">
          <circle cx="5" cy="5" r="4"/><circle cx="22" cy="5" r="4"/><circle cx="39" cy="5" r="4"/><circle cx="56" cy="5" r="4"/>
          <circle cx="73" cy="5" r="4"/><circle cx="90" cy="5" r="4"/><circle cx="107" cy="5" r="4"/><circle cx="124" cy="5" r="4"/>
        </g>
      </svg>
    </div>
  </section>

  <div class="submit-button">
    <span>Get Started</span>
    <svg width="13" height="17" viewBox="0 0 13 17" aria-hidden="true"><path d="M0 0 L13 8.5 L0 17 Z" fill="#111"/></svg>
  </div>

  <p class="signup-link">Not registered? Create Account</p>
</main>
</body>
</html>
```